Lunch Feature Menu and business card design

I am in need of a feature lunch menu for our cafe - 1902 Heron Cafe - I would like it to emulate the design of our current menu. I would also like it on an A5 paper size. I have attached a pdf of our current menu for you to see the style that it needs to follow and I have attached our logo as well which will also need to be on the menu. There are 5 feature items that will be going on the menu. The print for these items has been uploaded

Target Market(s)

downtown business crowd during the week and families on the weekend

Industry/Entity Type

Business

Contact Information for Business Card

cafe name : 1902 Heron Cafe
my name : Marisa Delgarno
title: General Manager and Partner
email :marisa.delgarno@1902heroncafe-example.ca
phone number : 403.555.2719
address : 264 Wendover Close Sw Calgary Alberta T2P7K9

Requirements
Nice to have
• Our cafe is a historic landmark in the city. It is very rustic - we would like to merge rustic and modern styles together for the menu and business card.

```html
<!DOCTYPE html>
<html lang="en">
<head>
<meta charset="utf-8">
<title>1902 Heron Cafe – Business Card</title>
<link rel="stylesheet" href="https://fonts.googleapis.com/css2?family=Arvo&family=Arimo:wght@700&display=swap">
<style>
  :root {
    --page: #ffffff;
    --heading: #2a2a2a;
    --ink: #2b2824;
    --ink-soft: #3a342c;
    --band: #1b1a18;
    --band-text: #e3a04b;
    --light-wood-1: #e4c991;
    --light-wood-2: #d7b679;
    --light-wood-3: #e6cc96;
    --dark-wood-1: #3d2619;
    --dark-wood-2: #2a1810;
    --name-light: #ffffff;
    --faint-text: rgba(196, 150, 80, 0.55);
    --mark: #8a6a45;
  }
  * { box-sizing: border-box; margin: 0; padding: 0; }
  html, body {
    width: 1200px; height: 1024px; overflow: hidden;
    background: var(--page);
    font-family: "Arvo", Georgia, serif;
    font-weight: 400;
    color: var(--ink);
  }
  .sheet { position: relative; width: 1200px; height: 1024px; }

  .side-label {
    position: absolute; left: 0; width: 1200px; text-align: center;
    font-family: "Arimo", Arial, sans-serif; font-weight: 700;
    font-size: 34px; letter-spacing: 0.5px; color: var(--heading);
  }
  .side-label--front { top: 118px; }
  .side-label--back { top: 540px; }

  .card { position: absolute; width: 523px; height: 299px; overflow: hidden; }
  .card--front-a { left: 62px; top: 186px; }
  .card--front-b { left: 614px; top: 186px; }
  .card--back-a { left: 62px; top: 600px; }
  .card--back-b { left: 614px; top: 600px; }

  .wood { position: absolute; inset: 0; }
  .wood--light {
    background: linear-gradient(175deg, var(--light-wood-1) 0%, var(--light-wood-2) 22%,
      var(--light-wood-3) 45%, var(--light-wood-2) 70%, var(--light-wood-1) 100%);
  }
  .wood--dark {
    background: linear-gradient(95deg, var(--dark-wood-1) 0%, var(--dark-wood-2) 30%,
      var(--dark-wood-1) 55%, var(--dark-wood-2) 80%, var(--dark-wood-1) 100%);
  }

  /* cafe name: single line, regular weight, plain circle beside */
  .cafe-name {
    position: absolute; display: flex; align-items: center; justify-content: center;
    font-weight: 400; color: var(--ink); white-space: nowrap;
  }
  .cafe-name__dot { flex: none; border-radius: 50%; background: var(--mark); }

  /* front A */
  .card--front-a .cafe-name { left: 10px; top: 138px; width: 168px; font-size: 16px; gap: 7px; }
  .card--front-a .cafe-name__dot { width: 14px; height: 14px; }
  .divider { position: absolute; left: 186px; top: 44px; width: 3px; height: 212px; background: var(--ink); }
  .contact { position: absolute; left: 204px; top: 74px; white-space: nowrap; }
  .contact__name { font-size: 20px; color: var(--ink); }
  .contact__title { font-size: 13.5px; margin-top: 4px; color: var(--ink-soft); }
  .contact__lines { margin-top: 20px; font-size: 12px; line-height: 18px; color: var(--ink-soft); }

  /* front B */
  .card--front-b .cafe-name { left: 0; width: 100%; top: 66px; font-size: 19px; gap: 9px; }
  .card--front-b .cafe-name__dot { width: 16px; height: 16px; }
  .card-name { position: absolute; left: 0; width: 100%; top: 158px; text-align: center; }
  .card-name__name { font-size: 22px; color: var(--ink); }
  .card-name__title { font-size: 15px; margin-top: 3px; color: var(--ink-soft); }
  .info-band {
    position: absolute; left: 0; right: 0; bottom: 0; height: 72px; background: var(--band);
    color: var(--band-text); font-size: 12px; line-height: 20px; white-space: nowrap;
  }
  .info-band__left { position: absolute; left: 16px; top: 15px; }
  .info-band__right { position: absolute; right: 16px; top: 15px; }

  /* back A */
  .card--back-a .cafe-name { left: 0; width: 100%; top: 128px; font-size: 34px; gap: 14px; color: var(--name-light); }
  .card--back-a .cafe-name__dot { width: 28px; height: 28px; background: var(--name-light); }

  /* back B */
  .card--back-b .cafe-name { left: 0; width: 100%; top: 118px; font-size: 34px; gap: 14px; }
  .card--back-b .cafe-name__dot { width: 28px; height: 28px; }
  .faint-info {
    position: absolute; top: 246px; font-size: 11.5px; line-height: 17px; color: var(--faint-text); white-space: nowrap;
  }
  .faint-info--left { left: 16px; }
  .faint-info--right { right: 16px; }
</style>
</head>
<body>
<main class="sheet">
  <h2 class="side-label side-label--front">FRONT</h2>

  <section class="card card--front-a">
    <div class="wood wood--light" role="img" aria-label="Light pine wood grain texture"></div>
    <div class="cafe-name"><span class="cafe-name__dot"></span>1902 Heron Cafe</div>
    <div class="divider"></div>
    <div class="contact">
      <p class="contact__name">Marisa Delgarno</p>
      <p class="contact__title">General Manager/Partner</p>
      <div class="contact__lines">
        <p>403.555.2719</p>
        <p>marisa.delgarno@1902heroncafe-example.ca</p>
        <p>264 Wendover Close SW</p>
        <p>T2P 7K9 Calgary AB</p>
      </div>
    </div>
  </section>

  <section class="card card--front-b">
    <div class="wood wood--light" role="img" aria-label="Light pine wood grain texture"></div>
    <div class="cafe-name"><span class="cafe-name__dot"></span>1902 Heron Cafe</div>
    <div class="card-name">
      <p class="card-name__name">Marisa Delgarno</p>
      <p class="card-name__title">General Manager/Partner</p>
    </div>
    <div class="info-band">
      <div class="info-band__left">
        <p>403.555.2719</p>
        <p>marisa.delgarno@1902heroncafe-example.ca</p>
      </div>
      <div class="info-band__right">
        <p>264 Wendover Close SW</p>
        <p>T2P 7K9 Calgary AB</p>
      </div>
    </div>
  </section>

  <h2 class="side-label side-label--back">BACK</h2>

  <section class="card card--back-a">
    <div class="wood wood--dark" role="img" aria-label="Dark walnut wood grain texture"></div>
    <div class="cafe-name"><span class="cafe-name__dot"></span>1902 Heron Cafe</div>
  </section>

  <section class="card card--back-b">
    <div class="wood wood--light" role="img" aria-label="Light pine wood grain texture"></div>
    <div class="cafe-name"><span class="cafe-name__dot"></span>1902 Heron Cafe</div>
    <div class="faint-info faint-info--left">
      <p>403.555.2719</p>
      <p>marisa.delgarno@1902heroncafe-example.ca</p>
    </div>
    <div class="faint-info faint-info--right">
      <p>264 Wendover Close SW</p>
      <p>T2P 7K9 Calgary AB</p>
    </div>
  </section>
</main>
</body>
</html>
```